Home page web design for a lawn specialist business

-The design must be based around the attached HPID (home page information design) called Turf Tidings HPID. I've attached Word and PDF versions - these are the same. The table boxes are just for approximate placement of information and you can use boxes and bold shapes for this design.

All fonts used in the HPID are only examples - you can use any Google font you wish.

- Text that is in orange is for your information only. Text to go on the design is black. Some instructions are in the HPID. Please be creative!

-The design needs to be modern and exciting - colours are to be the green of the logo, and white ...and then choose dark green, or dark grey or black.

Logo - attached (it's not great quality but don't worry, we'll replace it later)

- I've provided the images for the galleries - they are labelled and will match the name in the HPID. Please use the supplied images!

- Examples of some websites that have great design... don't copy them please but they are similar in look to what we are after....
www.qmbbuildworks.co.nz
http://www.rim-safeguard.co.nz/
http://www.lumenhomes.wb.gs/

Important: Width of content will be 1280 pixels when implemented as a web page but the winning design will need to supplied be on a 2000 pixel wide background so nav bars and background can extend outside the 1280 width.
Header height (without nav bar) 150-160 pixels.

We don't comment on individual designs but will choose a winning design promptly.

Industry/Entity Type

Business

Number of Pages Required

1 page

Font styles to use
Sans Serif

Requirements
Must have
• clean, modern, well-spaced design

```html
<!DOCTYPE html>
<html lang="en">
<head>
<meta charset="utf-8">
<title>Turf Tidings – Lawn specialists</title>
<link href="https://fonts.googleapis.com/css2?family=Gelasio:ital,wght@0,400;0,700;1,400;1,700&family=Lato:wght@400;700&display=swap" rel="stylesheet">
<style>
:root{
  --forest:#1f2f06;
  --forest-deep:#182504;
  --leaf:#3d8a06;
  --lime:#9ccc2a;
  --card:#efefef;
  --ink:#222;
  --muted:#555;
  --white:#fff;
}
*{box-sizing:border-box;margin:0;padding:0}
html,body{width:1200px;height:2597px;overflow:hidden}
body{position:relative;font-family:"Gelasio",Georgia,serif;color:var(--ink);background:var(--white)}
.abs{position:absolute}

/* header */
.site-header{left:0;top:0;width:1200px;height:120px;background:var(--forest);border-top:2px solid #3a4d17}
.brand{left:186px;top:40px;display:flex;align-items:center;gap:12px;color:var(--lime);font-size:30px;font-weight:700;letter-spacing:1px}
.brand-dot{width:18px;height:18px;border-radius:50%;background:var(--lime)}
.header-info{right:182px;top:10px;text-align:right;color:var(--white)}
.header-info h1{font-weight:400;font-size:29px;line-height:1.1}
.header-info p{font-size:13px;line-height:1.4}
.header-info .phone{font-size:21px;margin-top:6px}

/* nav */
.main-nav{left:0;top:120px;width:1200px;height:62px;background:var(--white);border-bottom:1px solid #ddd}
.main-nav ul{list-style:none;display:flex;justify-content:space-between;width:830px;margin-left:188px;height:62px;align-items:center}
.main-nav a{font-size:13px;font-style:italic;color:var(--ink);text-decoration:none;padding:18px 0 16px}
.main-nav .active{border-bottom:2px solid var(--forest)}

/* hero */
.hero{left:0;top:182px;width:1200px;height:378px;background:linear-gradient(100deg,#d9d6cf 0%,#5c4a3a 30%,#574535 55%,#4c8a2e 62%,#4f9a2c 100%)}
.hero-label{top:342px;color:var(--white);font-style:italic;font-weight:700;font-size:19px;letter-spacing:1px;text-shadow:0 1px 2px rgba(0,0,0,.5)}

/* intro */
.intro{left:0;top:560px;width:1200px;height:308px;background:var(--forest);color:var(--white);text-align:center}
.intro h2{margin-top:32px;font-size:29px;font-style:italic;font-weight:700}
.intro .lead{font-size:19px;margin-top:4px}
.intro p.body{width:700px;margin:26px auto 0;font-size:12px;line-height:1.85}
.intro p.body+p.body{margin-top:14px}

/* cards */
.card{width:406px;height:317px;background:var(--card);box-shadow:0 2px 5px rgba(0,0,0,.25);padding:18px 21px}
.card-photo{width:366px;height:128px}
.card h3{margin-top:14px;font-size:16px;font-weight:700;color:var(--forest)}
.rule{display:block;width:24px;height:3px;background:var(--forest);margin-top:7px;box-shadow:24px 1px 0 -1px #bbb}
.card p{margin-top:12px;font-size:11.5px;line-height:1.7;color:var(--muted);height:60px}
.btn-dark{display:inline-block;margin-top:14px;background:var(--forest);color:var(--white);font-size:11.5px;font-weight:700;font-style:italic;padding:10px 14px;border-radius:2px}

/* video band */
.video-band{left:0;top:1591px;width:1200px;height:347px;background:var(--forest);color:var(--white)}
.video{left:183px;top:37px;width:406px;height:273px;background:linear-gradient(160deg,#6f7a60,#3f6a25 55%,#2c3a1c)}
.video-bar{position:absolute;left:0;bottom:0;width:100%;height:22px;background:rgba(0,0,0,.75)}
.video-play{position:absolute;left:185px;top:115px;width:38px;height:38px;border-radius:50%;background:rgba(0,0,0,.55)}
.video-copy{left:611px;top:30px;width:410px}
.video-copy h2{font-size:25px;font-weight:700}
.video-copy .rule{background:var(--white);width:40px;box-shadow:40px 1px 0 -1px #777}
.video-copy p{font-size:12px;line-height:1.75;margin-top:20px}
.btn-light{display:inline-block;margin-top:22px;background:var(--white);color:var(--forest);font-size:14px;font-weight:700;font-style:italic;padding:9px 12px;border-radius:2px}

/* testimonial */
.testimonial{left:183px;top:1972px;width:410px}
.testimonial blockquote{font-size:17px;font-weight:700;font-style:italic;line-height:1.35;color:var(--ink)}
.testimonial .rule{width:40px;background:var(--ink);box-shadow:40px 1px 0 -1px #bbb;margin-top:8px}
.testimonial p{font-size:11.5px;line-height:1.6;color:var(--muted);margin-top:10px}
.testimonial cite{display:block;text-align:right;font-style:normal;font-size:16px;margin-top:6px}
.testimonial cite small{font-size:10.5px;color:var(--muted)}
.testimonial-photo{left:626px;top:1976px;width:376px;height:125px;background:linear-gradient(180deg,#a9b39b 0%,#6e9c3a 40%,#4d8a22 100%)}

/* footer */
.site-footer{left:0;top:2137px;width:1200px;height:460px;background:var(--leaf);color:var(--white);font-family:"Lato",Arial,sans-serif}
.footer-grass{left:0;bottom:0;width:1200px;height:110px;background:linear-gradient(180deg,rgba(61,138,6,0) 0%,#4f9a18 40%,#2f6a08 100%)}
.footer-col h2{font-weight:400;font-size:21px;padding-bottom:10px;border-bottom:1px solid rgba(255,255,255,.7)}
.quick-links{left:183px;top:35px;width:192px}
.quick-links ul{list-style:none}
.quick-links li{font-size:12px;padding:7px 0 6px 22px;border-bottom:1px solid rgba(255,255,255,.35);position:relative}
.quick-links li::before{content:"»";position:absolute;left:2px;top:5px;font-size:13px}
.badge-box{left:397px;top:39px;width:264px;height:276px;background:var(--white);border-radius:3px;display:flex;align-items:center;justify-content:center}
.contact{left:682px;top:35px;width:336px}
.contact .note{font-size:13px;line-height:1.45;margin-top:12px}
.form-grid{display:grid;grid-template-columns:1fr 1fr;gap:4px;margin-top:10px}
.field{background:var(--white);height:33px;font-size:10px;color:#aaa;padding:10px 8px}
.field.wide{grid-column:1/3;height:70px}
.btn-call{display:inline-block;margin-top:9px;background:var(--white);color:var(--ink);font-size:12px;font-weight:700;padding:11px 17px;border-radius:2px}
</style>
</head>
<body>

<header class="site-header abs">
  <div class="brand abs"><span class="brand-dot"></span>Turf Tidings</div>
  <div class="header-info abs">
    <h1>Lawn specialists</h1>
    <p>…from ground preparation to lawn aftercare</p>
    <p>Servicing the Auckland region</p>
    <p class="phone">0800 12 34 56</p>
  </div>
</header>

<nav class="main-nav abs">
  <ul>
    <li><a class="active" href="#">Home</a></li>
    <li><a href="#">About us</a></li>
    <li><a href="#">Services</a></li>
    <li><a href="#">Lawn care</a></li>
    <li><a href="#">Seasonal care</a></li>
    <li><a href="#">Hydroseeding</a></li>
    <li><a href="#">FAQs</a></li>
    <li><a href="#">Before &amp; After Gallery</a></li>
    <li><a href="#">Quote / Contact</a></li>
  </ul>
</nav>

<div class="hero abs" role="img" aria-label="Courtyard garden before and after lawn seeding: bare soil beds on the left, lush green lawn on the right"></div>
<span class="hero-label abs" style="left:434px">BEFORE</span>
<span class="hero-label abs" style="left:553px">AFTER</span>

<section class="intro abs">
  <h2>You can always spot an Turf Tidings lawn</h2>
  <p class="lead">It’s the one that turns your neighbours green with envy.</p>
  <p class="body">If you want a lawn or playing field that looks good throughout the year, talk to us. Turf Tidings are New Zealand’s experts in high quality grass seeding and lawn maintenance, creating the lushest lawns you’ll ever see. With high-tech equipment, years of experience and expert aftercare, nobody knows grass like Turf Tidings</p>
  <p class="body">There are many factors that influence the quality of a lawn, including seasonality, growing conditions, shade, seed types, and time. A one-size-fits-all solution couldn’t possibly guarantee a great lawn, so we provide personalised advice, a full range of seeding techniques</p>
</section>

<article class="card abs" style="left:182px;top:899px">
  <div class="card-photo" role="img" aria-label="Freshly hydroseeded garden bed in front of a house" style="background:linear-gradient(180deg,#8a8a7a 0%,#4e7d76 50%,#3f7068 100%)"></div>
  <h3>Grass seeding services</h3><span class="rule"></span>
  <p>With a wide range of grass seed applications to choose from, including hydro-seeding and instant lawn, there is an option to suit your property and your requirements.</p>
  <span class="btn-dark">MORE ABOUT GRASS SEEDING</span>
</article>

<article class="card abs" style="left:610px;top:899px">
  <div class="card-photo" role="img" aria-label="Garden sprinkler watering a green lawn" style="background:linear-gradient(180deg,#a6c97a 0%,#5f9a2c 55%,#3b7614 100%)"></div>
  <h3>Lawn care maintenance</h3><span class="rule"></span>
  <p>As well as lawn care services, the team at Turf Tidings provides helpful information for regular upkeep of your residential or commercial lawn.</p>
  <span class="btn-dark">MORE ABOUT GRASS SEEDING</span>
</article>

<article class="card abs" style="left:182px;top:1238px">
  <div class="card-photo" role="img" aria-label="Bright green lawn in a fenced backyard" style="background:linear-gradient(180deg,#b7b09f 0%,#7ea14a 50%,#4aa020 100%)"></div>
  <h3>FAQs about grass seeding and lawn care</h3><span class="rule"></span>
  <p>For more information, read our frequently asked questions regarding grass seeding and lawn care.</p>
  <span class="btn-dark">MORE ABOUT GRASS SEEDING</span>
</article>

<article class="card abs" style="left:610px;top:1238px">
  <div class="card-photo" role="img" aria-label="Side-by-side photos of a backyard before and after seeding" style="background:linear-gradient(90deg,#6e7a72 0%,#4d6e68 48%,#8ea06a 52%,#4f9a24 100%)"></div>
  <h3>Before and after lawn photos</h3><span class="rule"></span>
  <p>See what you potential new lawn could look like by viewing a range of before and after lawn seeding photos.</p>
  <span class="btn-dark">MORE ABOUT GRASS SEEDING</span>
</article>

<section class="video-band abs">
  <div class="video abs" role="img" aria-label="Embedded video of a finished front lawn">
    <span class="video-play"></span>
    <span class="video-bar"></span>
  </div>
  <div class="video-copy abs">
    <h2>Turf Tidings…</h2><span class="rule"></span>
    <p>For all things grass, you need the best! Turf Tidings are skilled specialists when it comes to creating the perfect lawn for your property.</p>
    <p>From pre-seeding preparation to a full range of grass seeding services and lawn after care options, you’ll enjoy a healthy green lawn for many years.</p>
    <p>Selling your property? Turf Tidings will add the wow factor to the outdoor areas of your home with a lush green lawn.</p>
    <span class="btn-light">Find out more</span>
  </div>
</section>

<section class="testimonial abs">
  <blockquote>"I would recommend Turf Tidings to anyone who wants an amazing lawn"</blockquote>
  <span class="rule"></span>
  <p>"Testimonial here about how great Turf Tidings were to deal with and how they are so happy with the lawn and the after care services etc etc."</p>
  <cite>Sam Porter <small>Homeowner, Albany</small></cite>
</section>
<div class="testimonial-photo abs" role="img" aria-label="Lawn mower on a freshly cut lawn beside a hedge"></div>

<footer class="site-footer abs">
  <div class="footer-grass abs" role="img" aria-label="Blades of grass along the bottom edge"></div>
  <div class="footer-col quick-links abs">
    <h2>Quick Links</h2>
    <ul>
      <li>Home</li><li>About us</li><li>Services</li><li>Lawn care</li><li>Seasonal care</li>
      <li>Hydroseeding</li><li>FAQs</li><li>Before &amp; After Gallery</li><li>Quote / Contact</li>
    </ul>
  </div>
  <div class="badge-box abs">
    <svg width="190" height="190" viewBox="0 0 190 190" aria-hidden="true"><circle cx="95" cy="95" r="88" fill="#8cc43a"/></svg>
  </div>
  <div class="footer-col contact abs">
    <h2>Contact Us</h2>
    <p class="note">Get a quote for your new lawn!<br>Fill in the form or phone us on 0800 12 34 56.</p>
    <div class="form-grid">
      <div class="field">First Name</div><div class="field">Last Name</div>
      <div class="field">Email Address</div><div class="field">Phone</div>
      <div class="field wide">Details</div>
    </div>
    <span class="btn-call">CALL ME BACK</span>
  </div>
</footer>

</body>
</html>
```